KVO-Business Card Design

I need a modern, professional business card design that includes my logo as the main feature, maybe the entire background with the contact info overlaying or even contact info on the back and the logo full frontal

Neat and organized placement of contact information

Would like to see options in black and white

Target Market(s)

real estate Developers, Construction managers, business and home owners

Industry/Entity Type

Construction

Contact Information for Business Card

KVO Construction
Danny Ferrante
General Contractor

Office: 1-888-902-7315 Ext #1
Cell: 215-730-4162
Fax: 1-888-902-7315

Font styles to use
Serif

Requirements
Must have
• title
• office #
• cell #
• Email
• website
Nice to have
• fax

```html
<!DOCTYPE html>
<html lang="en">
<head>
<meta charset="utf-8">
<title>KVO Construction – Business Card</title>
<link href="https://fonts.googleapis.com/css2?family=Arimo:wght@400;700&family=Michroma&display=swap" rel="stylesheet">
<style>
  :root {
    --backdrop: #3b3b3d;
    --card-white: #ffffff;
    --card-mist: #eceef2;
    --green-light: #8cc152;
    --green-mid: #4ea447;
    --green-deep: #1f7a3a;
    --brand-green: #2f8f3e;
    --ghost-grey: #e6e8e6;
    --ink-grey: #555a5e;
    --white: #ffffff;
  }
  * { margin: 0; padding: 0; box-sizing: border-box; }
  html, body { width: 1200px; height: 810px; overflow: hidden; }
  body { background: var(--backdrop); font-family: "Arimo", Arial, sans-serif; }

  .canvas { position: relative; width: 1200px; height: 810px; }

  .card {
    position: absolute;
    width: 540px;
    height: 310px;
    overflow: hidden;
    box-shadow: 0 14px 30px rgba(0,0,0,.45);
  }

  /* Front: brand side */
  .card--front { left: 50px; top: 140px; background: var(--card-white); }
  .front__ghost-name {
    position: absolute; left: 22px; top: 110px;
    font-family: "Arimo", Arial, sans-serif; font-weight: 700;
    font-size: 64px; line-height: 1; letter-spacing: 1px;
    color: var(--ghost-grey); white-space: nowrap;
  }
  .front__brand {
    position: absolute; right: 28px; top: 104px;
    display: flex; align-items: center; gap: 8px;
  }
  .brand-square { width: 16px; height: 16px; background: var(--brand-green); }
  .brand-name {
    font-family: "Arimo", Arial, sans-serif; font-weight: 700;
    font-size: 24px; color: var(--brand-green); white-space: nowrap;
  }
  .front__web {
    position: absolute; right: 30px; top: 142px;
    font-size: 14px; color: var(--ink-grey);
  }

  /* Back: contact side */
  .card--back { left: 610px; top: 360px; background: var(--card-mist); }
  .back__band { position: absolute; inset: 0; }
  .back__brand {
    position: absolute; left: 0; right: 0; top: 54px;
    display: flex; justify-content: center; align-items: center; gap: 8px;
  }
  .back__person {
    position: absolute; left: 40px; top: 232px; width: 240px; text-align: right;
    color: var(--white);
  }
  .person-name {
    font-family: "Michroma", "Arimo", sans-serif; font-size: 15px;
    letter-spacing: .5px; text-transform: uppercase; text-align: left;
  }
  .person-title { font-size: 12px; margin-top: 4px; margin-right: 10px; }

  .back__divider {
    position: absolute; left: 290px; top: 190px; width: 1px; height: 100px;
    background: rgba(255,255,255,.55);
  }
  .contact-list {
    position: absolute; left: 304px; top: 168px; list-style: none;
    color: var(--white); font-size: 13px;
  }
  .contact-list li {
    display: flex; align-items: center; gap: 7px; height: 22px; white-space: nowrap;
  }
  .contact-icon { width: 11px; height: 11px; flex: none; fill: var(--white); }
</style>
</head>
<body>
<main class="canvas">

  <section class="card card--front" aria-label="Business card front">
    <div class="front__ghost-name">KVO Construction</div>
    <div class="front__brand">
      <span class="brand-square"></span>
      <span class="brand-name">KVO Construction</span>
    </div>
    <div class="front__web">www.KVOConstruction.com</div>
  </section>

  <section class="card card--back" aria-label="Business card back">
    <svg class="back__band" width="540" height="310" viewBox="0 0 540 310" aria-hidden="true">
      <defs>
        <linearGradient id="bandGreen" x1="0" y1="0" x2="0" y2="1">
          <stop offset="0" stop-color="var(--green-light)"/>
          <stop offset=".55" stop-color="var(--green-mid)"/>
          <stop offset="1" stop-color="var(--green-deep)"/>
        </linearGradient>
      </defs>
      <path d="M0,225 Q140,212 255,178 L540,100 L540,310 L0,310 Z" fill="url(#bandGreen)"/>
      <path d="M0,218 Q140,205 255,171 L540,93" fill="none" stroke="#ffffff" stroke-width="2"/>
    </svg>

    <div class="back__brand">
      <span class="brand-square"></span>
      <span class="brand-name">KVO Construction</span>
    </div>

    <div class="back__person">
      <div class="person-name">Danny Ferrante</div>
      <div class="person-title">General Contractor</div>
    </div>

    <div class="back__divider"></div>

    <ul class="contact-list">
      <li>
        <svg class="contact-icon" viewBox="0 0 12 12" aria-hidden="true"><path d="M2,0 L4.5,0 L5,3 L3.5,4 Q5,7 8,8.5 L9,7 L12,7.5 L12,10 Q11,12 9,12 Q2,10 0,3 Q0,1 2,0 Z"/></svg>
        1-888-902-7315 Ext #1
      </li>
      <li>
        <svg class="contact-icon" viewBox="0 0 12 12" aria-hidden="true"><path d="M3,0 H9 V12 H3 Z M4,1.5 V9 H8 V1.5 Z"/></svg>
        215-730-4162
      </li>
      <li>
        <svg class="contact-icon" viewBox="0 0 12 12" aria-hidden="true"><path d="M3,0 H9 V4 H11 Q12,4 12,5 V10 H10 V12 H2 V10 H0 V5 Q0,4 1,4 H3 Z M3.5,8 V11 H8.5 V8 Z"/></svg>
        1-888-902-7315
      </li>
      <li>
        <svg class="contact-icon" viewBox="0 0 12 12" aria-hidden="true"><path d="M0,2 H12 V10 H0 Z M0.8,2.6 L6,6.6 L11.2,2.6 Z" fill-rule="evenodd"/></svg>
        support@KVOConstruction.com
      </li>
      <li>
        <svg class="contact-icon" viewBox="0 0 12 12" aria-hidden="true"><circle cx="6" cy="6" r="5.5" fill="none" stroke="#fff" stroke-width="1.2"/><path d="M0.5,6 H11.5 M6,0.5 Q2.5,6 6,11.5 M6,0.5 Q9.5,6 6,11.5" fill="none" stroke="#fff" stroke-width="1"/></svg>
        www.KVOConstruction.com
      </li>
    </ul>
  </section>

</main>
</body>
</html>
```